Vortique Energy Business Card Design

website: www.vortiqueenergy.example
Project: Business Card Design for Vortique Energy
Name: Derek Holloway
Title: Founder / Operations Strategist
Visual Identity & Logo:
Logo File: VRT-Logo-FullGradient-Final.png (Attached).
Color Palette: The brand relies on a distinctive Cyan (Blue) to Lime Green gradient.
Background Preference: We want a Dark Mode aesthetic (Deep Matte Black, Charcoal, or Dark Slate) to make the neon gradient of the logo pop. This feels more "tech/industrial" than a standard white card.
Design Aesthetic (The "Ops" Vibe):
Concept: "Grid & Infrastructure." We are a solar rental company, focusing on logistics and access.
Typography: White, bold sans-serif text for contact info. High contrast against the dark background.
Accents: Use the Cyan or Lime Green from the logo for thin divider lines or edge painting.
Avoid: No orange/gold (clashes with logo). No cartoon leaves.
Layout Requirements:
Front: Large, centered logo. Maybe a subtle UV gloss spot varnish over the logo icon.
Back: Name, Title, Contact Info.
Texture: Matte finish cardstock with gloss elements.
sample mock up of information on card: https://brimtolcorp-my.filedock.example/:i:/g/personal/derek_holloway_vortiqueenergy_com/AbCdEfGhIjKlMnOpQrStUvWxYz0123456789AbCdEfGh?e=X1Y2Z3
Logo: https://brimtolcorp.filedock.example/:i:/s/VortiqueEnergy/ZyXwVuTsRqPoNmLkJiHgFeDcBa9876543210ZyXwVuTs?e=Q4R5S6

```html
<!DOCTYPE html>
<html lang="en">
<head>
<meta charset="utf-8">
<title>Vortique Energy Business Card</title>
<link rel="stylesheet" href="https://fonts.googleapis.com/css2?family=Montserrat:wght@400;500;700&display=swap">
<style>
  :root {
    --backdrop: #9b9b9b;
    --card: #141414;
    --cyan: #15a0d8;
    --lime: #9cc83c;
    --text: #ececec;
    --pattern-light: #e4e4e4;
    --pattern-dark: #0c0c0c;
  }
  * { margin: 0; padding: 0; box-sizing: border-box; }
  html, body {
    width: 1200px;
    height: 1108px;
    overflow: hidden;
    background: var(--backdrop);
    font-family: "Montserrat", sans-serif;
  }
  .canvas { position: relative; width: 1200px; height: 1108px; }
  .card {
    position: absolute;
    left: 242px;
    width: 716px;
    height: 409px;
    border-radius: 30px;
    overflow: hidden;
    background: var(--card);
  }
  .card--front { top: 119px; }
  .card--back { top: 580px; }

  .front-pattern {
    position: absolute;
    inset: 0;
    background:
      radial-gradient(ellipse 70% 90% at 10% 30%, var(--pattern-light) 0%, rgba(200,200,200,0.75) 35%, rgba(60,60,60,0.5) 65%, transparent 85%),
      linear-gradient(100deg, #3a3a3a 0%, #1a1a1a 55%, var(--pattern-dark) 100%);
  }

  .front-brand {
    position: absolute;
    left: 0;
    right: 0;
    top: 188px;
    display: flex;
    justify-content: center;
    align-items: center;
    gap: 10px;
  }
  .front-brand__mark {
    width: 26px;
    height: 26px;
    background: var(--cyan);
  }
  .front-brand__name {
    font-size: 26px;
    font-weight: 500;
    color: var(--cyan);
    white-space: nowrap;
  }

  .brand {
    position: absolute;
    left: 40px;
    top: 186px;
    display: flex;
    align-items: center;
    gap: 12px;
  }
  .brand__mark {
    width: 22px;
    height: 22px;
    background: var(--cyan);
  }
  .brand__name {
    font-size: 30px;
    font-weight: 500;
    color: var(--cyan);
    letter-spacing: 0.2px;
    white-space: nowrap;
  }

  .divider {
    position: absolute;
    left: 346px;
    top: 80px;
    width: 2px;
    height: 251px;
    background: linear-gradient(to bottom, var(--cyan), var(--lime));
  }

  .details {
    position: absolute;
    left: 374px;
    top: 71px;
    color: var(--text);
  }
  .details__name {
    font-size: 31px;
    font-weight: 700;
    color: var(--cyan);
    line-height: 40px;
    white-space: nowrap;
  }
  .details__title {
    font-size: 18.5px;
    font-weight: 400;
    line-height: 26px;
    white-space: nowrap;
  }
  .details__address {
    margin-top: 16px;
    font-size: 18.5px;
    line-height: 28.5px;
    white-space: nowrap;
  }
  .contact-list {
    list-style: none;
    margin-top: 11px;
  }
  .contact-list li {
    display: flex;
    align-items: center;
    gap: 9px;
    font-size: 18.5px;
    line-height: 28.5px;
    white-space: nowrap;
  }
  .contact-list svg { width: 16px; height: 16px; flex: none; }
</style>
</head>
<body>
<main class="canvas">
  <section class="card card--front">
    <div class="front-pattern" role="img" aria-label="Glossy silver-to-black field of repeated geometric brand shapes"></div>
    <div class="front-brand">
      <span class="front-brand__mark"></span>
      <span class="front-brand__name">Vortique Energy</span>
    </div>
  </section>

  <section class="card card--back">
    <div class="brand">
      <span class="brand__mark"></span>
      <span class="brand__name">Vortique Energy</span>
    </div>

    <div class="divider"></div>

    <div class="details">
      <h1 class="details__name">Derek Holloway</h1>
      <p class="details__title">Founder / Operations Strategist</p>
      <p class="details__address">Vortique Energy, LLC 4180<br>Marrowind Avenue Brellton,<br>FL 30517</p>
      <ul class="contact-list">
        <li>
          <svg viewBox="0 0 16 16" aria-hidden="true"><path d="M1 5.5C1 3.5 4 2.5 8 2.5s7 1 7 3v1.2h-3.2V5.3H4.2v1.4H1z" fill="#1aa7d2"/><rect x="3" y="7.5" width="10" height="6" rx="1" fill="#6cbf5a"/><circle cx="8" cy="10.5" r="1.6" fill="#141414"/></svg>
          555.014.2273
        </li>
        <li>
          <svg viewBox="0 0 16 16" aria-hidden="true"><rect x="1" y="3.5" width="14" height="9" fill="#8cc63f"/><path d="M1 3.5l7 5 7-5" fill="none" stroke="#141414" stroke-width="1.2"/></svg>
          info@vortiqueenergy.example
        </li>
        <li>
          <svg viewBox="0 0 16 16" aria-hidden="true"><circle cx="8" cy="8" r="6.5" fill="#1aa7d2"/><path d="M4 5c2 0 2 2 4 2s1 3 -1 4-1 3-1 3M10 3c0 2 2 2 3 3" fill="none" stroke="#8cc63f" stroke-width="2"/></svg>
          www.vortiqueenergy.example
        </li>
      </ul>
    </div>
  </section>
</main>
</body>
</html>
```